Clean Landing Page - Design and Code

Need to create a similar landing page to example i have supplied. Need versions for Desktop, tablet and mobile. Letting the design chose color scheme based on description.

We want it to seem fresh, clean and cool.

We are basing it off this example http://torvanmesk.com/

Target Market(s)

young ambitious entreprerial women

Coding

Coded - Design and coding required

Number of Pages Required

3 page

Font styles to use
Sans Serif

Requirements
Must have
• Must be designed for responsive functionality.

```html
<!DOCTYPE html>
<html lang="en">
<head>
<meta charset="utf-8">
<title>Curabur Nonfggs Pretium</title>
<link rel="stylesheet" href="https://fonts.googleapis.com/css2?family=Josefin+Slab:wght@400;600;700&display=swap">
<style>
  :root {
    --hero-deep: #8549a7;
    --hero-mid: #c68fcd;
    --hero-rose: #a2388f;
    --title-plum: #4d2066;
    --white: #ffffff;
    --ink: #111111;
    --rule-light: #c9c9c9;
    --page: #ffffff;
  }
  * { margin: 0; padding: 0; box-sizing: border-box; }
  html, body {
    width: 1200px; height: 603px; overflow: hidden;
    background: var(--page);
    font-family: "Josefin Slab", Georgia, serif;
  }
  .page { position: relative; width: 1200px; height: 603px; overflow: hidden; }

  .hero {
    position: absolute; left: 0; top: 0; width: 1200px; height: 309px;
    background:
      radial-gradient(ellipse 300px 220px at 80px 90px, rgba(176,40,120,.75), rgba(176,40,120,0) 70%),
      radial-gradient(ellipse 420px 260px at 620px 130px, rgba(222,170,220,.85), rgba(222,170,220,0) 75%),
      linear-gradient(90deg, #9a4aa4 0%, var(--hero-mid) 45%, #b17ac0 70%, var(--hero-deep) 82%, var(--hero-deep) 100%);
  }

  .main-nav {
    position: absolute; top: 17px; left: 0; width: 1200px;
    display: flex; justify-content: center; gap: 0;
  }
  .main-nav a {
    position: absolute; transform: translateX(-50%);
    color: var(--white); text-decoration: none;
    font-size: 10.5px; font-weight: 600; letter-spacing: .3px;
    text-transform: uppercase; white-space: nowrap;
  }

  .rule-stack { position: absolute; left: 0; width: 1200px; height: 20px; }
  .rule-stack span { position: absolute; height: 1px; }
  .hero .rule-stack span { background: rgba(255,255,255,.85); }
  .intro .rule-stack span { background: var(--rule-light); }

  .hero-title {
    position: absolute; top: 112px; left: 0; width: 1200px;
    text-align: center; color: var(--title-plum);
    font-size: 47px; font-weight: 700; line-height: 54px;
    letter-spacing: 1.5px; text-transform: uppercase;
  }
  .hero-lede {
    position: absolute; top: 241px; left: 0; width: 1200px;
    text-align: center; color: var(--white);
    font-size: 11.3px; line-height: 20px;
  }

  .intro-heading {
    position: absolute; top: 389px; left: 0; width: 1200px;
    text-align: center; color: var(--ink);
    font-size: 22.5px; font-weight: 600; letter-spacing: .6px;
    text-transform: uppercase;
  }
  .portrait {
    position: absolute; width: 146px; height: 146px; border-radius: 50%;
    top: 447px;
  }
  .portrait--lavender { left: 310px; background: radial-gradient(circle at 35% 40%, #d6c0de, #b497c0 60%, #efe6ee); }
  .portrait--winter { left: 538px; background: radial-gradient(circle at 60% 55%, #4a4650, #8a9fa4 55%, #c8d4d4); }
  .portrait--sunlit { left: 750px; background: radial-gradient(circle at 50% 45%, #f3e8d6, #e2cfa6 55%, #b89c74); }
</style>
</head>
<body>
<div class="page">
  <header class="hero" role="img" aria-label="Close-up portrait of a woman with a red flower, tinted purple">
    <nav class="main-nav">
      <a href="#" style="left:457px">Welcome</a>
      <a href="#" style="left:532px">About</a>
      <a href="#" style="left:603px">Services</a>
      <a href="#" style="left:679px">Gallery</a>
      <a href="#" style="left:758px">Contact</a>
    </nav>
    <div class="rule-stack" style="top:73px">
      <span style="left:571px;width:63px;top:0"></span>
      <span style="left:555px;width:95px;top:6px"></span>
      <span style="left:523px;width:159px;top:13px"></span>
    </div>
    <h1 class="hero-title">Curabur Nonfggs<br>Pretium</h1>
    <p class="hero-lede">Morbi sodales enim in turpis mattis, fermentum auctor elit commodo. Nam lacinia pretium egestas.<br>Fusce rhoncus elementum consectetur. Duis facilisis varius porttitor.</p>
  </header>

  <section class="intro">
    <div class="rule-stack" style="top:344px">
      <span style="left:571px;width:63px;top:0"></span>
      <span style="left:555px;width:95px;top:6px"></span>
      <span style="left:523px;width:159px;top:13px"></span>
    </div>
    <h2 class="intro-heading">Nunc eleifend quis diam in commodo.</h2>
    <div class="portrait portrait--lavender" role="img" aria-label="Photo of a young woman with long hair among soft purple flowers"></div>
    <div class="portrait portrait--winter" role="img" aria-label="Photo of a young woman in a fur coat in falling snow"></div>
    <div class="portrait portrait--sunlit" role="img" aria-label="Photo of two smiling friends in warm sunlight"></div>
  </section>
</div>
</body>
</html>
```